Flyer for Makeup Class

A flyer for my makeup class promotion. I am a make up artist starting a group class to teach makeup to ladies. I have attached some verbiage handwritten. My picture is the one in pink hijab. I have also attached some inspiration ideas and color combination (the colors in the cake design are the ones I want to use).

Target Market(s)

Ladies looking to learn make up from a make up artist

Industry/Entity Type

Hair And Beauty

Requirements
Must have
• The verbiage / description that I have hand written should be written using graphics and nice fonts. You can change the exact wording to make it better.

```html
<!DOCTYPE html>
<html lang="en">
<head>
<meta charset="utf-8">
<title>Makeup Masterclass Flyer</title>
<link href="https://fonts.googleapis.com/css2?family=Montserrat:wght@400;500;600;700;800&family=Pinyon+Script&display=swap" rel="stylesheet">
<style>
  :root{
    --page:#e9e9ea;
    --plum-deep:#3b0629;
    --plum:#52103f;
    --magenta:#e2097f;
    --blush:#f6c3c0;
    --violet:#7b1f7f;
    --skin-1:#c89a86;
    --skin-2:#7a4a52;
    --white:#ffffff;
  }
  *{margin:0;padding:0;box-sizing:border-box;}
  html,body{width:1200px;height:1050px;overflow:hidden;background:var(--page);}
  .canvas{position:relative;width:1200px;height:1050px;}
  .flyer{position:absolute;left:243px;top:20px;width:714px;height:1010px;overflow:hidden;background:var(--plum-deep);font-family:"Montserrat",sans-serif;color:var(--white);box-shadow:0 6px 24px rgba(0,0,0,.18);}
  .flyer-shapes{position:absolute;inset:0;}
  .title-script{position:absolute;left:390px;top:36px;width:300px;text-align:center;font-family:"Pinyon Script",cursive;font-size:28px;line-height:32px;}
  .title-script .artist{font-size:32px;}
  .venue{position:absolute;left:42px;top:478px;}
  .venue-label{font-weight:800;font-size:56px;letter-spacing:2px;line-height:60px;}
  .venue-place{font-weight:500;font-size:20px;letter-spacing:.5px;margin-top:2px;}
  .venue-date{font-weight:700;font-size:32px;margin-top:4px;}
  .ribbon-text{position:absolute;left:70px;top:614px;width:580px;text-align:center;font-weight:600;font-size:26px;line-height:33px;}
  .description{position:absolute;left:42px;top:708px;width:620px;font-size:14px;line-height:20px;font-weight:500;}
  .booking{position:absolute;left:392px;top:834px;width:315px;}
  .booking-head{font-size:15px;font-weight:500;letter-spacing:.3px;}
  .booking-line{display:flex;align-items:center;gap:8px;margin-top:6px;font-weight:700;font-size:18px;}
  .booking-line.email{font-size:15px;font-weight:600;}
  .booking-line svg{flex:none;}
  .call-now{margin-top:8px;font-size:18px;font-weight:500;white-space:nowrap;}
  .call-now strong{font-size:26px;font-weight:800;margin-left:6px;}
</style>
</head>
<body>
<div class="canvas">
  <div class="flyer">
    <svg class="flyer-shapes" width="714" height="1010" viewBox="0 0 714 1010">
      <defs>
        <linearGradient id="portraitTone" x1="0" y1="0" x2="1" y2="1">
          <stop offset="0" stop-color="var(--skin-1)"/>
          <stop offset=".6" stop-color="var(--skin-2)"/>
          <stop offset="1" stop-color="var(--plum)"/>
        </linearGradient>
        <linearGradient id="lowerPlum" x1="0" y1="0" x2="1" y2="0">
          <stop offset="0" stop-color="#3e0730"/>
          <stop offset="1" stop-color="#6a2a55"/>
        </linearGradient>
        <linearGradient id="classTone" x1="0" y1="0" x2="1" y2="1">
          <stop offset="0" stop-color="#d9d4d2"/>
          <stop offset="1" stop-color="#8a6f78"/>
        </linearGradient>
        <linearGradient id="artistTone" x1="0" y1="0" x2="0" y2="1">
          <stop offset="0" stop-color="#8aa37a"/>
          <stop offset="1" stop-color="#f2c9c4"/>
        </linearGradient>
      </defs>
      <rect width="714" height="1010" fill="url(#lowerPlum)"/>
      <rect x="0" y="0" width="714" height="420" fill="var(--plum)"/>
      <path role="img" aria-label="Close-up beauty portrait with purple lips and nails" d="M0,0 H420 V300 C300,320 150,380 0,450 Z" fill="url(#portraitTone)"/>
      <g stroke="var(--white)" stroke-width="1.2" fill="none">
        <line x1="30" y1="95" x2="330" y2="95"/>
        <line x1="60" y1="80" x2="60" y2="360"/>
        <line x1="410" y1="28" x2="700" y2="28"/>
        <line x1="688" y1="16" x2="688" y2="190"/>
      </g>
      <path d="M0,430 C170,350 380,300 714,270 L714,300 C390,328 180,380 0,462 Z" fill="var(--magenta)"/>
      <path d="M0,462 C180,380 390,328 714,300 L714,316 C395,343 190,396 0,480 Z" fill="var(--blush)"/>
      <path d="M0,480 C190,396 395,343 714,316 L714,1010 H0 Z" fill="url(#lowerPlum)"/>
      <circle cx="565" cy="300" r="98" fill="var(--blush)"/>
      <circle role="img" aria-label="Makeup class in progress" cx="565" cy="300" r="91" fill="url(#classTone)"/>
      <polygon points="20,604 694,604 672,647 694,690 20,690 42,647" fill="var(--magenta)"/>
      <path d="M0,980 H714 V1010 H0 Z" fill="var(--violet)"/>
      <path d="M200,1010 C260,900 330,820 430,800 C560,776 660,742 714,692 L714,1010 Z" fill="var(--violet)"/>
      <path d="M200,1010 C260,900 330,820 430,800 C560,776 660,742 714,692" fill="none" stroke="var(--blush)" stroke-width="4"/>
      <circle cx="250" cy="880" r="122" fill="var(--blush)"/>
      <circle role="img" aria-label="Portrait of the makeup artist in a pink hijab" cx="250" cy="880" r="115" fill="url(#artistTone)"/>
    </svg>

    <div class="title-script">
      Exclusive<br>Makeup Masterclass<br>by<br><span class="artist">Sana Mirza</span><br>( UK based MUA )
    </div>

    <div class="venue">
      <div class="venue-label">VENUE:</div>
      <div class="venue-place">RIVERSIDE CLUB GARDEN COMPLEX (ISLAMABAD)</div>
      <div class="venue-date">6th April 2019 - 11:30 - 5.30 pm</div>
    </div>

    <div class="ribbon-text">Perfect For Professionals, Beginners And<br>Make Up Lovers</div>

    <p class="description">This Class Is Packed With Loads Of Information Tips, Live Demos, Goodie Bag, Certificate, Q&amp;A, Lunch And Much More.....</p>

    <div class="booking">
      <div class="booking-head">TO BOOK YOUR PLACE CONTACT:</div>
      <div class="booking-line">
        <svg width="16" height="16" viewBox="0 0 16 16"><circle cx="8" cy="8" r="8" fill="var(--magenta)"/><path d="M5.2,4 l1.6,0 .6,2 -1,.8 c.5,1.2 1.3,2 2.5,2.5 l.8,-1 2,.6 0,1.6 c-4,.4 -7,-2.6 -6.5,-6.5z" fill="var(--white)"/></svg>
        <span>03001234567</span>
      </div>
      <div class="booking-line email">
        <svg width="16" height="16" viewBox="0 0 16 16"><circle cx="8" cy="8" r="8" fill="var(--magenta)"/><rect x="4" y="5.5" width="8" height="5.5" fill="var(--white)"/><path d="M4,5.5 l4,3 4,-3" stroke="var(--magenta)" stroke-width="1" fill="none"/></svg>
        <span>hello@sanamirzamua.com</span>
      </div>
      <div class="call-now">CALL NOW <strong>07700900466</strong></div>
    </div>
  </div>
</div>
</body>
</html>
```